Veltrix Global Policy Document/Report Template for consistent document outputs

We need a policy document/report template that we can disseminate to staff so all produced documents look the same, and less formatting has to be done each time a policy or report is started.
VGL applies the power of biological science, physical science, and IT to solve the most challenging mission problems encompassing Forensics, Biometrics, Weapons Technical and Identity Intelligence, CBRNE, CWMD, and Public Health initiatives. Here is a list of requirements for the document:
• Cover page
o Include full logo
o Title
o Possibly a subtitle
o Version #
o Date
o We want a common look that all policy documents will follow, and it is easy to recognize
o Some color and a unique look and feel
• Header and Footer (2nd page on)
o Both header and footer must include this language: “Confidential and Proprietary - For Veltrix Global Internal Use Only,” so it appears at the top and bottom of the page
o The document title must be in either the header or footer
• Header (after first page)
o Include logo
• Footer (not counting title page)
o Must include date, and page X of Y
• 4 levels of headings, numbered 1, 1.1, 1.1.1, 1.1.1.1
• 4 levels of bullets with color/style
• Design for a callout box
• Design or a box containing a quote
• Two table designs
• Pages (other than the title page)
o Pages are primarily white
o Colors for accent and visual interest

Finally, our corporate font is Source Sans Pro.
The swirl pattern on our logo has no special meaning (but feel free to use it as a design element).

Font styles to use
Other font styles liked:
• Source Sans Pro

Requirements
Must have
• See description for more information: Cover page, header and footer, multiple heading levels, callout box, tables

```html
<!DOCTYPE html>
<html lang="en">
<head>
<meta charset="utf-8">
<title>Veltrix Global Policy Document Template</title>
<link rel="stylesheet" href="https://fonts.googleapis.com/css2?family=Source+Sans+3:ital,wght@0,300;0,400;0,600;0,700;1,400&display=swap">
<style>
:root{
  --navy:#23166e;
  --purple:#3f2ea0;
  --purple-soft:#c9c3ea;
  --red:#bc0b31;
  --ink:#333333;
  --muted:#6b6b6b;
  --paper:#ffffff;
  --backdrop:#ececec;
  --row:#efefef;
}
*{margin:0;padding:0;box-sizing:border-box}
html,body{width:1200px;height:1058px;overflow:hidden;background:var(--backdrop)}
body{font-family:"Source Sans 3","Source Sans Pro",sans-serif;color:var(--ink)}
.sheet-board{position:absolute;left:0;top:0;width:2044px;height:1803px;transform:scale(.58708);transform-origin:0 0}
.page{position:absolute;width:488px;height:690px;background:var(--paper);overflow:hidden}
.p-cover{left:157px;top:140px}
.p-blank{left:770px;top:140px}
.p-headings{left:1384px;top:140px}
.p-callout{left:157px;top:929px}
.p-quote{left:770px;top:929px}
.p-tables{left:1384px;top:929px}
.abs{position:absolute}

/* brand name mark */
.brand{position:absolute;display:flex;align-items:center;gap:6px;font-weight:700;color:var(--navy);line-height:1}
.brand-dot{display:block;border-radius:50%;background:var(--red)}
.cover-brand{left:48px;top:58px;font-size:40px}
.cover-brand .brand-dot{width:16px;height:16px}
.head-brand{left:48px;top:62px;font-size:32px}
.head-brand .brand-dot{width:12px;height:12px}

/* cover */
.cover-title{left:314px;top:46px;color:var(--navy);font-size:42px;line-height:39px;white-space:nowrap}
.cover-title b{font-weight:700;display:block}
.cover-title span{font-weight:300;display:block}
.cover-sub{left:316px;top:120px;font-size:10.5px;font-style:italic;color:var(--navy);white-space:nowrap}
.cover-rule{left:316px;top:136px;width:57px;height:3px;background:var(--navy)}
.cover-version{left:316px;top:153px;font-size:16px;font-weight:300;color:var(--navy);white-space:nowrap}
.cover-shapes{left:0;top:0}
.cover-cal{left:400px;top:610px}
.cover-date{left:362px;top:631px;font-size:16px;font-weight:300;color:var(--navy);white-space:nowrap}
.cover-date-rule{left:388px;top:652px;width:44px;height:2px;background:var(--navy)}

/* running header/footer */
.conf{position:absolute;left:0;width:100%;text-align:center;font-size:8px;color:var(--muted);white-space:nowrap}
.conf-top{top:32px}
.conf-foot{top:650px;left:128px;width:auto;text-align:left}
.page-no{position:absolute;left:412px;top:650px;font-size:8px;color:var(--muted);white-space:nowrap}
.doc-title{left:161px;top:64px;font-size:28px;color:var(--ink);letter-spacing:.3px;white-space:nowrap}
.doc-title b{font-weight:600}
.doc-title span{font-weight:300}
.doc-date{right:54px;top:107px;font-size:13px;font-weight:300;color:var(--ink);white-space:nowrap}

/* headings */
.toc{left:81px;top:178px;font-size:28px;font-weight:300;color:var(--ink);line-height:50px;list-style:none;white-space:nowrap}
.toc b{font-weight:600}

/* bullets, four levels */
.bullets{left:84px;top:395px;font-size:15px;font-weight:400;color:var(--ink);line-height:26px;list-style:none;white-space:nowrap}
.bullets li{position:relative;padding-left:18px}
.bullets li::before{content:"";position:absolute;left:0;top:10px}
.bullets .lv1::before{width:8px;height:8px;border-radius:50%;background:var(--navy)}
.bullets .lv2{margin-left:22px}
.bullets .lv2::before{width:7px;height:7px;background:var(--red)}
.bullets .lv3{margin-left:44px}
.bullets .lv3::before{width:8px;height:8px;border-radius:50%;border:2px solid var(--purple)}
.bullets .lv4{margin-left:66px}
.bullets .lv4::before{top:12px;width:9px;height:2px;background:var(--red)}

/* callout box */
.callout-box{left:75px;top:280px;width:322px;height:130px;background:var(--purple);border-left:8px solid var(--red)}
.callout-text{left:135px;top:302px;width:215px;color:#fff}
.callout-text h2{font-size:24px;line-height:26px;letter-spacing:.3px;white-space:nowrap}
.callout-text h2 b{font-weight:600}
.callout-text h2 span{font-weight:300}
.callout-text p{font-size:10.5px;line-height:11.6px;font-weight:300;margin-top:2px}

/* quote bubble */
.bubble{left:0;top:0}
.quote-text{left:111px;top:278px;width:255px;color:#fff}
.quote-text h2{font-size:24px;line-height:28px;letter-spacing:.3px;white-space:nowrap}
.quote-text h2 b{font-weight:600}
.quote-text h2 span{font-weight:300}
.quote-text p{font-size:9.6px;line-height:11.6px;font-weight:300;margin-top:8px}

/* card table */
.card-table{left:57px;top:169px;width:379px;height:227px;border:1px solid var(--purple-soft);border-radius:10px;overflow:hidden;display:grid;grid-template-columns:repeat(5,1fr);grid-template-rows:90px 1fr}
.card-head{background:var(--purple);color:#fff;padding:16px 0 0 18px;font-size:11px;line-height:11px;position:relative}
.card-head:not(:first-child)::before{content:"";position:absolute;left:0;top:28px;height:34px;width:1px;background:rgba(255,255,255,.7)}
.card-head b{font-weight:600;display:block}
.card-head span{font-weight:300;display:block}
.card-head em{font-style:normal;font-weight:300;display:block;margin-top:7px}
.card-cell{padding:14px 6px 0;text-align:center;font-size:3.6px;line-height:4.4px;color:var(--muted);border-right:1px solid var(--purple-soft)}
.card-cell:nth-child(10){border-right:none}
.card-cell p{height:24px}
.card-cell i{display:block;width:34px;height:1px;background:var(--purple);margin:3px auto 14px}

/* grid table */
.grid-table{left:57px;top:446px;border-collapse:separate;border-spacing:3px 0;margin-left:-3px}
.grid-table th{background:var(--purple);color:#fff;font-size:5.5px;font-weight:600;height:17px;padding:0;white-space:nowrap}
.grid-table th:first-child{width:89px}
.grid-table th:not(:first-child){width:69px}
.grid-table td{height:17px;font-size:6px;color:var(--muted);padding-left:23px;white-space:nowrap}
.grid-table tr.shade td{background:var(--row);background-clip:content-box;padding:2px 0}
.grid-table tr.shade td:first-child span{padding-left:23px}
</style>
</head>
<body>
<main class="sheet-board">

  <section class="page p-cover">
    <svg class="abs cover-shapes" width="488" height="690" viewBox="0 0 488 690" aria-hidden="true">
      <circle cx="258" cy="485" r="147" fill="var(--red)"/>
      <circle cx="40" cy="383" r="216" fill="var(--navy)"/>
    </svg>
    <div class="brand cover-brand"><i class="brand-dot"></i>VGL</div>
    <h1 class="abs cover-title"><b>LOREM</b><span>IPSUM</span></h1>
    <p class="abs cover-sub">quis nostrud exercitation ullamco</p>
    <div class="abs cover-rule"></div>
    <p class="abs cover-version">VERSION: #0000</p>
    <svg class="abs cover-cal" width="20" height="19" viewBox="0 0 20 19" aria-hidden="true">
      <rect x="1" y="3" width="18" height="15" fill="none" stroke="var(--navy)" stroke-width="1.6"/>
      <line x1="1" y1="7" x2="19" y2="7" stroke="var(--navy)" stroke-width="1.6"/>
      <line x1="6" y1="0" x2="6" y2="4" stroke="var(--navy)" stroke-width="1.6"/>
      <line x1="14" y1="0" x2="14" y2="4" stroke="var(--navy)" stroke-width="1.6"/>
      <g fill="var(--navy)"><rect x="4" y="9" width="2" height="2"/><rect x="9" y="9" width="2" height="2"/><rect x="14" y="9" width="2" height="2"/><rect x="4" y="13" width="2" height="2"/><rect x="9" y="13" width="2" height="2"/><rect x="14" y="13" width="2" height="2"/></g>
    </svg>
    <p class="abs cover-date">00 - 00- 2024</p>
    <div class="abs cover-date-rule"></div>
  </section>

  <section class="page p-blank">
    <p class="conf conf-top">Confidential and Proprietary - For Veltrix Global Internal Use Only</p>
    <div class="brand head-brand"><i class="brand-dot"></i>VGL</div>
    <h2 class="abs doc-title"><b>LOREM</b> <span>IPSUM</span></h2>
    <p class="abs doc-date">00 - 00- 2024</p>
    <p class="conf conf-foot">Confidential and Proprietary - For Veltrix Global Internal Use Only</p>
    <p class="page-no">Page 1 of 5</p>
  </section>

  <section class="page p-headings">
    <p class="conf conf-top">Confidential and Proprietary - For Veltrix Global Internal Use Only</p>
    <div class="brand head-brand"><i class="brand-dot"></i>VGL</div>
    <h2 class="abs doc-title"><b>LOREM</b> <span>IPSUM</span></h2>
    <p class="abs doc-date">00 - 00- 2024</p>
    <ol class="abs toc">
      <li><b>1</b> Lorem Ipsum</li>
      <li><b>1.1</b> Lorem Ipsum</li>
      <li><b>1.1.1</b> Lorem Ipsum</li>
      <li><b>1.1.1.1</b> Lorem Ipsum</li>
    </ol>
    <ul class="abs bullets">
      <li class="lv1">Lorem ipsum dolor</li>
      <li class="lv2">Lorem ipsum dolor</li>
      <li class="lv3">Lorem ipsum dolor</li>
      <li class="lv4">Lorem ipsum dolor</li>
    </ul>
    <p class="conf conf-foot">Confidential and Proprietary - For Veltrix Global Internal Use Only</p>
    <p class="page-no">Page 2 of 5</p>
  </section>

  <section class="page p-callout">
    <p class="conf conf-top">Confidential and Proprietary - For Veltrix Global Internal Use Only</p>
    <div class="brand head-brand"><i class="brand-dot"></i>VGL</div>
    <h2 class="abs doc-title"><b>LOREM</b> <span>IPSUM</span></h2>
    <p class="abs doc-date">00 - 00- 2024</p>
    <div class="abs callout-box"></div>
    <div class="abs callout-text">
      <h2><b>LOREM</b> <span>IPSUM</span></h2>
      <p>Lorem ipsum dolor sit amet, consectetur adipiscing elit, sed do eiusmod tempor incididunt ut labore et dolore magna aliqua. Ut enim ad minim veniam, quis nostrud exercitation ullamco laboris nisi ut aliquip ex ea commodo consequat.</p>
    </div>
    <p class="conf conf-foot">Confidential and Proprietary - For Veltrix Global Internal Use Only</p>
    <p class="page-no">Page 3 of 5</p>
  </section>

  <section class="page p-quote">
    <p class="conf conf-top">Confidential and Proprietary - For Veltrix Global Internal Use Only</p>
    <div class="brand head-brand"><i class="brand-dot"></i>VGL</div>
    <h2 class="abs doc-title"><b>LOREM</b> <span>IPSUM</span></h2>
    <p class="abs doc-date">00 - 00- 2024</p>
    <svg class="abs bubble" width="488" height="690" viewBox="0 0 488 690" aria-hidden="true">
      <rect x="85" y="238" width="303" height="250" rx="45" fill="var(--purple)"/>
      <path d="M190 487 L280 487 L242 535 Q237 541 232 535 Z" fill="var(--purple)"/>
      <path d="M270 209 H330 V268 Q330 300 288 311 L274 297 Q300 285 300 268 H270 Z" fill="var(--red)"/>
      <path d="M342 209 H402 V268 Q402 300 360 311 L346 297 Q372 285 372 268 H342 Z" fill="var(--red)"/>
    </svg>
    <div class="abs quote-text">
      <h2><b>LOREM</b> <span>IPSUM</span></h2>
      <p>Lorem ipsum dolor sit amet, consectetur adipiscing elit, sed do eius mod tempor incididunt ut labore et dolore magna aliqua. Ut enim ad minim veniam, quis nostrud exercitation ullamco laboris nisi ut aliquip ex ea commodo consequat.</p>
      <p>Ut enim ad minim veniam, quis nostrud exercitation ullamco laboris nisi ut aliquip ex ea commodo consequat.</p>
      <p>Lorem ipsum dolor sit amet, consectetur adipiscing elit, sed do eius mod tempor incididunt ut labore et dolore magna aliqua. Ut enim ad minim veniam.</p>
    </div>
    <p class="conf conf-foot">Confidential and Proprietary - For Veltrix Global Internal Use Only</p>
    <p class="page-no">Page 4 of 5</p>
  </section>

  <section class="page p-tables">
    <p class="conf conf-top">Confidential and Proprietary - For Veltrix Global Internal Use Only</p>
    <div class="brand head-brand"><i class="brand-dot"></i>VGL</div>
    <h2 class="abs doc-title"><b>LOREM</b> <span>IPSUM</span></h2>
    <p class="abs doc-date">00 - 00- 2024</p>

    <div class="abs card-table">
      <div class="card-head"><b>LOREM</b><span>IPSUM</span><em>dolor sit<br>amet</em></div>
      <div class="card-head"><b>LOREM</b><span>IPSUM</span><em>dolor sit<br>amet</em></div>
      <div class="card-head"><b>LOREM</b><span>IPSUM</span><em>dolor sit<br>amet</em></div>
      <div class="card-head"><b>LOREM</b><span>IPSUM</span><em>dolor sit<br>amet</em></div>
      <div class="card-head"><b>LOREM</b><span>IPSUM</span><em>dolor sit<br>amet</em></div>
      <div class="card-cell"><p>Lorem ipsum dolor sit amet elit.</p><i></i><p>Lorem ipsum dolor sit amet elit.</p><i></i><p>Lorem ipsum dolor sit amet elit.</p></div>
      <div class="card-cell"><p>Lorem ipsum dolor sit amet elit.</p><i></i><p>Lorem ipsum dolor sit amet elit.</p><i></i><p>Lorem ipsum dolor sit amet elit.</p></div>
      <div class="card-cell"><p>Lorem ipsum dolor sit amet elit.</p><i></i><p>Lorem ipsum dolor sit amet elit.</p><i></i><p>Lorem ipsum dolor sit amet elit.</p></div>
      <div class="card-cell"><p>Lorem ipsum dolor sit amet elit.</p><i></i><p>Lorem ipsum dolor sit amet elit.</p><i></i><p>Lorem ipsum dolor sit amet elit.</p></div>
      <div class="card-cell"><p>Lorem ipsum dolor sit amet elit.</p><i></i><p>Lorem ipsum dolor sit amet elit.</p><i></i><p>Lorem ipsum dolor sit amet elit.</p></div>
    </div>

    <table class="abs grid-table">
      <thead><tr><th>LOREM IPSUM</th><th>LOREM IPSUM</th><th>LOREM IPSUM</th><th>LOREM IPSUM</th><th>LOREM IPSUM</th></tr></thead>
      <tbody>
        <tr class="shade"><td><span>Lorem Ipsum</span></td><td></td><td></td><td></td><td></td></tr>
        <tr><td>Lorem Ipsum</td><td></td><td></td><td></td><td></td></tr>
        <tr class="shade"><td><span>Lorem Ipsum</span></td><td></td><td></td><td></td><td></td></tr>
        <tr><td>Lorem Ipsum</td><td></td><td></td><td></td><td></td></tr>
        <tr class="shade"><td><span>Lorem Ipsum</span></td><td></td><td></td><td></td><td></td></tr>
        <tr><td>Lorem Ipsum</td><td></td><td></td><td></td><td></td></tr>
        <tr class="shade"><td><span>Lorem Ipsum</span></td><td></td><td></td><td></td><td></td></tr>
      </tbody>
    </table>

    <p class="conf conf-foot">Confidential and Proprietary - For Veltrix Global Internal Use Only</p>
    <p class="page-no">Page 5 of 5</p>
  </section>

</main>
</body>
</html>
```